Real Estate Company Looking for Business Card Designs for 3 Executives

Hello!
Thanks so much for considering our project! We are a real estate investment company located in Edmonton, Alberta called Marlbeck Group of Companies. We invest/develop both commercial and residential real estate and are looking to create 3 DOUBLE-SIDED business cards for 3 top executives in the company! (for some reason it won't let us select the double-sided option, but yes, the cards are double sided and would be happy to tip extra)

We have certain guidelines that we want our business cards to for sure follow - the back of the Business card has to be the Black Background Version of the Logo which has already been designed and linked as a file (first file). We want the entire back of the card to simply just be the black background logo. In terms of the front of the card, would like to see a smaller version of the white background logo (linked as the second file) in the top left hand corner - of course, feel free to get creative and we can make revisions together along the way! and Then after that, just text. We want the card to be sharp, clean, easy on the eyes and highly professional looking. We would like the card to include the Full name of the Company (Marlbeck Group of Companies), Name of the Person, Title, Phone, Email. If possible please provide the front part of the card for 3 people:

1) Marlbeck Group of Companies, Lena Okafor, Chief Financial Officer, 780-555-0162, lenaokafor@marlbeckgroup.example

2) Marlbeck Group of Companies, Tobias Okafor, Chief Executive Officer, 780-555-0148, tobiasokafor@marlbeckgroup.example

3) Marlbeck Group of Companies, Rui Dalton, Chief Operations Officer, 587-555-0193, ruidalton@marlbeckgroup.example

Thank you so much for considering our project & we look forward to seeing your designs!

```html
<!DOCTYPE html>
<html lang="en">
<head>
<meta charset="utf-8">
<title>Marlbeck Group of Companies — Business Card</title>
<link href="https://fonts.googleapis.com/css2?family=Arimo:wght@400;500&family=Tinos:wght@700&display=swap" rel="stylesheet">
<style>
  :root {
    --backdrop: #1b1b1b;
    --card-front: #ffffff;
    --card-back: #1f1f1f;
    --ink: #1c1c1c;
    --ink-soft: #2a2a2a;
    --back-mark: #3b3b3b;
  }
  * { box-sizing: border-box; margin: 0; padding: 0; }
  html, body { width: 1200px; height: 1059px; overflow: hidden; }
  body { background: var(--backdrop); position: relative; font-family: "Arimo", Arial, sans-serif; }

  .card { position: absolute; width: 690px; height: 392px; }
  .card--front { left: 256px; top: 89px; background: var(--card-front); color: var(--ink); }
  .card--back { left: 254px; top: 547px; background: var(--card-back); }

  .brand { position: absolute; display: flex; align-items: center; gap: 10px; }
  .brand__square { width: 12px; height: 12px; background: var(--ink); flex: none; }
  .brand__name { font-family: "Arimo", Arial, sans-serif; font-weight: 500; color: var(--ink); letter-spacing: 0.22em; text-transform: uppercase; line-height: 1.35; }
  .card--front .brand { right: 36px; top: 92px; }
  .card--front .brand__name { font-size: 15px; text-align: left; }

  .card--back .brand { left: 0; right: 0; top: 0; bottom: 0; justify-content: center; gap: 18px; }
  .card--back .brand__square { width: 22px; height: 22px; background: var(--back-mark); }
  .card--back .brand__name { color: var(--back-mark); font-size: 34px; letter-spacing: 0.24em; }

  .person { position: absolute; left: 36px; top: 200px; }
  .person__name { font-family: "Tinos", "Times New Roman", serif; font-weight: 700; font-size: 29px; line-height: 1.2; color: var(--ink); }
  .person__title { font-size: 17.5px; color: var(--ink-soft); margin-top: 2px; }
  .person__rule { width: 13px; height: 2px; background: var(--ink); margin: 12px 0 12px; }

  .contact { list-style: none; }
  .contact__item { display: flex; align-items: center; gap: 7px; font-size: 17.5px; height: 28px; color: var(--ink-soft); }
  .contact__icon { width: 14px; height: 14px; flex: none; fill: var(--ink); }
</style>
</head>
<body>
  <section class="card card--front">
    <div class="brand">
      <span class="brand__square"></span>
      <span class="brand__name">Marlbeck<br>Group of Companies</span>
    </div>
    <div class="person">
      <h1 class="person__name">Tobias Okafor</h1>
      <p class="person__title">Chief Executive Officer</p>
      <div class="person__rule"></div>
      <ul class="contact">
        <li class="contact__item">
          <svg class="contact__icon" viewBox="0 0 24 24"><path d="M6.6 10.8a15.1 15.1 0 0 0 6.6 6.6l2.2-2.2a1 1 0 0 1 1-.25 11.4 11.4 0 0 0 3.6.57 1 1 0 0 1 1 1V20a1 1 0 0 1-1 1A17 17 0 0 1 3 4a1 1 0 0 1 1-1h3.5a1 1 0 0 1 1 1c0 1.25.2 2.45.57 3.57a1 1 0 0 1-.25 1z"/></svg>
          <span>780-555-0148</span>
        </li>
        <li class="contact__item">
          <svg class="contact__icon" viewBox="0 0 24 24"><path d="M2 5h20v14H2z M3.5 6.5 12 13l8.5-6.5" fill="none" stroke="#1c1c1c" stroke-width="2"/><path d="M2 5h20L12 12.5z"/></svg>
          <span>tobiasokafor@marlbeckgroup.example</span>
        </li>
        <li class="contact__item">
          <svg class="contact__icon" viewBox="0 0 24 24"><circle cx="12" cy="12" r="10"/><path d="M8 6c2 1 1 3 3 3s1 3-1 3-2 3 0 5M15 5c-1 2 1 3 2 3s2 2 1 4-2 2-2 4" fill="none" stroke="#fff" stroke-width="1.6"/></svg>
          <span>www.marlbeckgroup.example</span>
        </li>
      </ul>
    </div>
  </section>

  <section class="card card--back">
    <div class="brand">
      <span class="brand__square"></span>
      <span class="brand__name">Marlbeck</span>
    </div>
  </section>
</body>
</html>
```